Motor Mate 4x6 Flyer

Need 4 x 6 Flyer with following language:

Willow Crest Motor Mate
Our Motor Mate Will Come to Your Home
Our Motor Mate will Drive Your Car to Nearest Gas Station
Our Motor Mate will Fill-up Your Car with Gas
Our Motor Mate will Immediately Return Your Car
Your Car Covered with $100k of Commercial Insurance
Member Dunmore Chamber of Commerce / Honest Merchant League
www.willowcrestmotormate.example

Place logos of Vortan, Brenn & Dorvane on Left Side of Flyer starting at top left corner, mid left side, left bottom corner.
Place logos of BoltNest, 12-Forty, Tesmira on opposite side right.....
Place Willow Crest Motor Mate Logo on both sides of very top that says Willow Crest Motor Mate

Target Market(s)

Upscale Home Owners

Font styles to use
Sans Serif

Colors
F0912C
F2A743
F7CA91
FBE8D2
FDF5EE

Requirements
Must have
• Flyer Must be Bright Orange

```html
<!DOCTYPE html>
<html lang="en">
<head>
<meta charset="utf-8">
<title>Willow Crest Motor Mate – 4x6 Flyer</title>
<link rel="stylesheet" href="https://fonts.googleapis.com/css2?family=Poppins:ital,wght@0,400;0,600;0,700;0,800;1,900&family=Quicksand:wght@700&display=swap">
<style>
  :root {
    --orange: #F0912C;
    --orange-deep: #e8761c;
    --orange-light: #F2A743;
    --peach: #F7CA91;
    --cream: #FBE8D2;
    --red: #f0262a;
    --ink: #111111;
    --white: #ffffff;
    --stage: #000000;
    --brand-blue: #1b5fb4;
    --brand-green: #2a8a3a;
  }
  * { box-sizing: border-box; margin: 0; padding: 0; }
  html, body { width: 892px; height: 1200px; overflow: hidden; background: var(--stage); }
  body { position: relative; font-family: "Poppins", sans-serif; }

  .flyer { position: absolute; left: 77px; width: 741px; overflow: hidden; }
  .flyer--front { top: 67px; height: 495px; background: var(--white); }
  .flyer--back { top: 637px; height: 491px; background: var(--orange); }

  .photo-fill {
    position: absolute; inset: 0;
    background:
      radial-gradient(ellipse at 25% 20%, #4f6a2a 0%, rgba(79,106,42,0) 35%),
      radial-gradient(ellipse at 60% 45%, #e5431e 0%, rgba(229,67,30,0) 40%),
      radial-gradient(ellipse at 45% 70%, #3a2a1a 0%, rgba(58,42,26,0) 35%),
      linear-gradient(135deg, #c97a2a 0%, #e59a3a 45%, #b8631f 100%);
  }
  .shape-layer { position: absolute; inset: 0; width: 100%; height: 100%; }

  .brand-mark { position: absolute; left: 0; right: 0; display: flex; flex-direction: column; align-items: center; }
  .brand-mark__square { width: 50px; height: 58px; border: 5px solid var(--red); border-radius: 7px; }
  .brand-mark__name {
    font-family: "Quicksand", sans-serif; font-weight: 700; font-size: 31px;
    color: var(--ink); letter-spacing: 0.5px; line-height: 1; margin-top: 22px;
  }
  .flyer--front .brand-mark { top: 28px; }
  .flyer--back .brand-mark { top: 30px; }

  .headline {
    position: absolute; left: 0; right: 0; text-align: center;
    font-weight: 900; font-style: italic; color: var(--white);
    letter-spacing: -1.5px; line-height: 1; text-transform: uppercase;
  }
  .flyer--front .headline { top: 220px; font-size: 43px; text-shadow: 0 2px 6px rgba(0,0,0,.25); }
  .flyer--back .headline { top: 190px; font-size: 33px; text-shadow: 3px 5px 6px rgba(0,0,0,.35); }

  .web-pill {
    position: absolute; left: 50%; transform: translateX(-50%);
    background: var(--red); color: var(--white);
    font-size: 14.5px; font-weight: 400; padding: 1px 8px; white-space: nowrap; line-height: 20px;
  }
  .flyer--front .web-pill { top: 459px; }
  .flyer--back .web-pill { top: 462px; }

  .partner-row { position: absolute; top: 446px; display: flex; gap: 12px; align-items: center; }
  .partner-row--left { left: 16px; }
  .partner-row--right { right: 16px; }
  .partner { font-weight: 700; font-size: 13px; line-height: 1; white-space: nowrap; }
  .partner--red { color: var(--red); }
  .partner--blue { color: var(--brand-blue); }
  .partner--ink { color: var(--ink); }
  .partner--green { color: var(--brand-green); }

  .steps { position: absolute; top: 246px; left: 0; right: 0; }
  .step { position: absolute; width: 180px; margin-left: -90px; text-align: center; }
  .step:nth-child(1) { left: 91px; }
  .step:nth-child(2) { left: 247px; }
  .step:nth-child(3) { left: 424px; }
  .step:nth-child(4) { left: 609px; }
  .step__icon { width: 78px; height: 66px; margin: 0 auto; background: var(--orange-deep); border-radius: 6px; }
  .step__text {
    margin-top: 10px; font-weight: 700; font-size: 14px; line-height: 21px;
    letter-spacing: -0.5px; color: var(--ink);
  }

  .insurance {
    position: absolute; top: 400px; left: 0; right: 0; text-align: center;
    font-weight: 700; font-size: 22.5px; letter-spacing: -0.8px; color: var(--ink);
  }
  .membership {
    position: absolute; top: 439px; left: 0; right: 0; text-align: center;
    font-weight: 400; font-size: 13.5px; letter-spacing: -0.3px; color: var(--ink);
  }
</style>
</head>
<body>

<section class="flyer flyer--front">
  <div class="photo-fill" role="img" aria-label="Photograph of a hand holding a fuel nozzle filling a car at the pump, warm orange toning"></div>
  <svg class="shape-layer" viewBox="0 0 741 495" preserveAspectRatio="none" aria-hidden="true">
    <path d="M0,0 H741 V28 C660,80 620,110 570,138 C490,178 430,178 371,178 C300,176 235,150 185,95 C145,45 70,24 0,22 Z" fill="var(--white)"/>
    <path d="M741,28 C660,80 620,110 570,138 C490,178 430,178 371,178 C300,176 235,150 185,95 C145,45 70,24 0,22" fill="none" stroke="var(--orange)" stroke-width="8"/>
    <path d="M0,335 C70,328 120,338 155,372 C195,418 245,440 290,446 C325,455 338,478 343,495 H0 Z" fill="var(--white)"/>
    <path d="M0,335 C70,328 120,338 155,372 C195,418 245,440 290,446" fill="none" stroke="var(--orange)" stroke-width="4"/>
    <path d="M741,335 C692,330 662,346 642,380 C612,430 562,436 522,450 C505,460 500,480 503,495 H741 Z" fill="var(--white)"/>
    <path d="M741,335 C692,330 662,346 642,380 C612,430 562,436 522,450" fill="none" stroke="var(--orange)" stroke-width="4"/>
  </svg>

  <div class="brand-mark">
    <div class="brand-mark__square"></div>
    <div class="brand-mark__name">Motor Mate</div>
  </div>

  <h1 class="headline">Willow Crest Motor Mate</h1>

  <div class="partner-row partner-row--left">
    <span class="partner partner--red">Vortan</span>
    <span class="partner partner--red">Brenn</span>
    <span class="partner partner--blue">Dorvane</span>
  </div>
  <div class="partner-row partner-row--right">
    <span class="partner partner--ink">BoltNest</span>
    <span class="partner partner--green">12-Forty</span>
    <span class="partner partner--blue">Tesmira</span>
  </div>

  <div class="web-pill">www.willowcrestmotormate.example</div>
</section>

<section class="flyer flyer--back">
  <svg class="shape-layer" viewBox="0 0 741 491" preserveAspectRatio="none" aria-hidden="true">
    <path d="M0,8 H741 V34 C690,60 640,95 590,130 C530,165 450,175 371,175 C300,175 240,150 190,110 C140,70 90,40 0,25 Z" fill="var(--white)"/>
    <path d="M741,34 C690,60 640,95 590,130 C530,165 450,175 371,175 C300,175 240,150 190,110 C140,70 90,40 0,25" fill="none" stroke="var(--red)" stroke-width="8"/>
  </svg>

  <div class="brand-mark">
    <div class="brand-mark__square"></div>
    <div class="brand-mark__name">Motor Mate</div>
  </div>

  <h2 class="headline">Willow Crest Motor Mate</h2>

  <div class="steps">
    <div class="step">
      <div class="step__icon" role="img" aria-label="Icon of a valet in a suit beside a house and car"></div>
      <p class="step__text">Our Motor Mate<br>Will Come to<br>Your Home</p>
    </div>
    <div class="step">
      <div class="step__icon" role="img" aria-label="Icon of a car at a gas station building"></div>
      <p class="step__text">Our Motor Mate<br>will Drive Your Car<br>to Nearest Gas Station</p>
    </div>
    <div class="step">
      <div class="step__icon" role="img" aria-label="Icon of an attendant fuelling a car at a pump"></div>
      <p class="step__text">Our Motor Mate<br>will Fill-up Your Car<br>with Gas</p>
    </div>
    <div class="step">
      <div class="step__icon" role="img" aria-label="Icon of a car returned to a home"></div>
      <p class="step__text">Our Motor Mate<br>will Immediately Return<br>Your Car</p>
    </div>
  </div>

  <p class="insurance">Your Car Covered with $100k of Commercial Insurance</p>
  <p class="membership">Member Dunmore Chamber of Commerce / Honest Merchant League</p>
  <div class="web-pill">www.willowcrestmotormate.example</div>
</section>

</body>
</html>
```